Electrical contractor needs a flyer and business card

'Voltique - The Electrical Contractor' needs an a5 flyer designed which will showcase the work we undertake. We already have a logo - see attached
We operate in Devon and Cornwall in the UK in these 3 market sectors: Domestic, Commercial, Industrial.
The work we undertake is as follows:
House re-wires
New builds
RCD and consumer unit upgrades
Renovations
TV aerials & extra points
Data / phone / networking
Security and garden lighting
Extra external / internal sockets
Garage upgrades
LED and low energy lighting installs
We offer a free consumer unit and earthing check!
24 hour service.
prompt quality service with over 15 years experience
All our work is fully certified and guaranteed for a year
contact details:
Marcus Pelling
Owner
marcus@voltique-wiring.co.uk
www.voltique-wiring.co.uk
m: 07938661207
t: 01392 586 031
Servicing Devon & Cornwall
We also need a business card designed
many thanks
Raf
Target Market(s)
Domestic, Commercial, Industrial.
Industry/Entity Type
Contractor
Font styles to use
Other font styles liked:
- eurostile extended
Look and feel

```html
<!DOCTYPE html>
<html lang="en">
<head>
<meta charset="utf-8">
<title>Voltique - The Electrical Contractor</title>
<link rel="stylesheet" href="https://fonts.googleapis.com/css2?family=Michroma&family=Raleway:wght@300;600;700;800&display=swap">
<style>
  :root {
    --teal-edge: #9ccfcf;
    --teal-soft: #d9eeee;
    --teal-text: #84c3c8;
    --teal-blue: #1f8db4;
    --rule: #acd9e1;
    --grey-text: #9a9fa1;
    --grey-mark: #a4a8aa;
    --dark-text: #3b3d3e;
    --icon-dark: #4a4c4d;
    --white: #ffffff;
  }
  * { margin: 0; padding: 0; box-sizing: border-box; }
  html, body { width: 846px; height: 1200px; overflow: hidden; }
  body { font-family: "Raleway", sans-serif; background: var(--teal-edge); }
  .flyer {
    position: relative; width: 846px; height: 1200px; overflow: hidden;
    background: radial-gradient(ellipse 476px 594px at 50% 50%, var(--white) 0%, #f6f9f9 80%, #e6f2f2 95%, var(--teal-edge) 100%);
  }
  .line { position: absolute; left: 0; width: 846px; text-align: center; white-space: nowrap; }
  .accent { color: var(--teal-text); }
  .accent-blue { color: var(--teal-blue); }
  .brand-dot {
    position: absolute; left: 373px; top: 42px; width: 100px; height: 100px;
    border-radius: 50%; background: var(--teal-soft);
  }
  .brand-name {
    top: 186px; font-family: "Michroma", sans-serif; font-size: 44px;
    letter-spacing: 14px; color: var(--grey-mark); padding-left: 14px;
  }
  .tagline {
    top: 240px; font-family: "Michroma", sans-serif; font-size: 21px;
    letter-spacing: 1.5px; color: var(--teal-blue);
  }
  .rule { position: absolute; left: 30px; width: 786px; height: 2px; background: var(--rule); }
  .intro { font-size: 22px; font-weight: 700; color: var(--grey-text); }
  .including { font-size: 17px; font-weight: 300; color: var(--teal-text); }
  .service { font-size: 20.5px; font-weight: 700; color: var(--grey-text); }
  .badge {
    position: absolute; width: 176px; height: 176px; border-radius: 50%;
    background: radial-gradient(circle at 50% 30%, #ffffff 0%, #e7f1f1 45%, #a9cccb 100%);
    border: 2px solid #e9f1f1;
    box-shadow: 0 0 0 2px #b6cfcf, 0 4px 6px rgba(0,0,0,0.25);
    display: flex; flex-direction: column; align-items: center; justify-content: center;
    text-align: center; color: var(--dark-text); font-weight: 700; font-size: 17.5px; line-height: 20px;
  }
  .badge-big { font-size: 47px; font-weight: 800; line-height: 48px; letter-spacing: 1px; }
  .badge-sub { font-size: 27px; font-weight: 800; line-height: 28px; letter-spacing: 1px; }
  .call-prompt { font-size: 20.5px; font-weight: 700; color: var(--grey-text); }
  .phone { position: absolute; top: 900px; display: flex; align-items: center; gap: 12px; }
  .phone-number { font-size: 40px; font-weight: 800; color: var(--teal-text); letter-spacing: 1px; }
  .email-label { font-size: 21px; font-weight: 600; color: var(--grey-text); }
  .email { font-size: 32px; font-weight: 600; color: #8b8f91; letter-spacing: 1px; }
  .website { font-size: 20px; font-weight: 600; color: var(--teal-text); letter-spacing: 0.5px; }
</style>
</head>
<body>
<main class="flyer">
  <div class="brand-dot"></div>
  <h1 class="line brand-name">VOLTIQUE</h1>
  <div class="line tagline">THE ELECTRICAL CONTRACTOR</div>

  <div class="rule" style="top:287px"></div>
  <p class="line intro" style="top:305px">WE’RE BASED IN DEVON <span class="accent">&amp;</span> CORNWALL,</p>
  <p class="line intro" style="top:339px">OFFERING DOMESTIC, COMMERCIAL <span class="accent">&amp;</span> INDUSTRIAL SERVICES</p>
  <p class="line including" style="top:376px">- INCLUDING -</p>
  <div class="rule" style="top:410px"></div>

  <ul class="services">
    <li class="line service" style="top:426px">HOUSE RE-WIRES <span class="accent-blue">•</span> NEW BUILDS <span class="accent-blue">•</span> RCD &amp; CONSUMER UNIT UPGRADES</li>
    <li class="line service" style="top:460px">DATA <span class="accent">/</span> PHONE <span class="accent">/</span> NETWORKING <span class="accent-blue">•</span> SECURITY <span class="accent">&amp;</span> GARDEN LIGHTING</li>
    <li class="line service" style="top:494px">EXTRA EXTERNAL <span class="accent">&amp;</span> INTERNAL SOCKETS <span class="accent-blue">•</span> GARAGE UPGRADES</li>
    <li class="line service" style="top:528px">RENOVATIONS <span class="accent-blue">•</span> TV AERIALS <span class="accent">&amp;</span> EXTRA POINTS</li>
    <li class="line service" style="top:562px">LED <span class="accent">&amp;</span> LOW ENERGY LIGHTING INSTALLS</li>
  </ul>
  <div class="rule" style="top:603px"></div>

  <div class="badge" style="left:37px;top:629px">WE OFFER<br>A <span class="accent-blue">FREE</span><br>CONSUMER<br>UNIT &amp;<br>EARTHING<br>CHECK!</div>
  <div class="badge" style="left:235px;top:629px"><span class="badge-big">24HR</span><span class="badge-sub">SERVICES</span></div>
  <div class="badge" style="left:435px;top:629px">PROMPT,<br>QUALITY<br>SERVICE WITH<br>OVER <span class="accent-blue">15 YEARS</span><br>EXPERIENCE!</div>
  <div class="badge" style="left:634px;top:629px">ALL WORK<br>IS FULLY<br><span class="accent-blue">CERTIFIED &amp;<br>GUARANTEED</span><br>FOR A YEAR!</div>

  <div class="rule" style="top:837px"></div>
  <p class="line call-prompt" style="top:863px">NEED SOME WORK DONE<span class="accent">?</span> CALL US NOW, ON<span class="accent">:</span></p>

  <div class="phone" style="left:22px">
    <svg width="70" height="70" viewBox="0 0 70 70" aria-hidden="true">
      <circle cx="35" cy="35" r="32" fill="none" stroke="var(--icon-dark)" stroke-width="4"/>
      <path d="M24 17c3-2 5-1 6 1l3 7c1 2 0 3-2 4l-2 1c1 5 5 10 9 12l2-2c1-2 3-2 4-1l6 4c2 1 2 3 0 5l-3 3c-3 2-8 1-13-3-6-5-12-13-13-20-1-4 1-9 3-11z" fill="var(--icon-dark)"/>
    </svg>
    <span class="phone-number">07938661207</span>
  </div>
  <div class="phone" style="left:420px">
    <svg width="70" height="70" viewBox="0 0 70 70" aria-hidden="true">
      <circle cx="35" cy="35" r="32" fill="none" stroke="var(--icon-dark)" stroke-width="4"/>
      <path d="M24 17c3-2 5-1 6 1l3 7c1 2 0 3-2 4l-2 1c1 5 5 10 9 12l2-2c1-2 3-2 4-1l6 4c2 1 2 3 0 5l-3 3c-3 2-8 1-13-3-6-5-12-13-13-20-1-4 1-9 3-11z" fill="var(--icon-dark)"/>
    </svg>
    <span class="phone-number">01392 586 031</span>
  </div>

  <p class="line email-label" style="top:989px">OR EMAIL US, AT<span class="accent">:</span></p>
  <p class="line email" style="top:1018px">marcus<span class="accent">@</span>voltique-wiring.co.uk</p>
  <p class="line website" style="top:1067px">WWW.VOLTIQUE-WIRING.CO.UK</p>
</main>
</body>
</html>
```